Corbrook Estates LLC stationary for a real estate property management company.

Create stationary (letterhead, envelopes, business cards) using Corbrook Estates LLC logo as primary creative element. Stationary design needs to be horizontal, leaving as much space as possible for correspondence copy. See attached Creative Brief and past stationary files for details.

Target Market(s)

Prospective apartment residents and current residents, vendors, and government agencies.

Industry/Entity Type

Property Management

Contact Information for Business Card

Business card employee title: Property Manager. Should include address, phone, fax, email, website, slogan, and Corbrook Estates logo.

Font styles to use
Sans Serif

Colors
0592cd
000000

Requirements
Must have
• Tone should be conservative, institutional, business (i.e. banking, finance, real estate). Must include: address, phone, fax, website, and slogan (see attached Creative Brief). Should be a horizontal design, leaving as much room as possible for letter correspondence copy.
Nice to have
• Please use an Arial or Helvetica style font.
Should not have
• Letterhead layout should leave as much room as possible for copy.

```html
<!DOCTYPE html>
<html lang="en">
<head>
<meta charset="utf-8">
<title>Corbrook Estates LLC Stationery</title>
<link href="https://fonts.googleapis.com/css2?family=Arimo:wght@400;700&family=PT+Sans:wght@400&display=swap" rel="stylesheet">
<style>
  :root{
    --blue:#0a6aa8;
    --blue-dark:#0b5c93;
    --charcoal:#414244;
    --paper:#f6f6f6;
    --card-grey:#ececec;
    --ink:#3a3a3a;
    --body-ink:#4a4a4a;
    --backdrop:#d9d6d2;
  }
  *{box-sizing:border-box;margin:0;padding:0}
  html,body{width:1200px;height:754px;overflow:hidden;background:var(--backdrop)}
  .canvas{position:relative;width:1200px;height:754px;font-family:"Arimo",Arial,sans-serif;color:var(--ink)}
  .sheet{position:absolute;background:var(--paper);box-shadow:0 2px 6px rgba(0,0,0,.25);overflow:hidden}
  .wordmark{color:var(--blue);font-weight:700;line-height:1;display:flex;align-items:center;gap:6px}
  .wordmark .dot{width:0.9em;height:0.9em;border-radius:50%;background:var(--blue);flex:none}
  .wordmark .name{display:flex;flex-direction:column}
  .wordmark .sub{font-size:.42em;letter-spacing:.22em;margin-top:2px}
  .band{position:absolute;left:0;bottom:0;width:100%}
  .contact{list-style:none;font-size:7.5px;line-height:10.2px}
  .contact li{display:flex;align-items:center;gap:5px}
  .contact svg{width:7px;height:7px;flex:none}

  /* letterhead */
  .letterhead{left:36px;top:32px;width:488px;height:688px}
  .letterhead .wordmark{position:absolute;left:46px;top:64px;font-size:23px}
  .letterhead .divider{position:absolute;left:316px;top:44px;width:1px;height:66px;background:#c9c9c9}
  .letterhead .address{position:absolute;left:326px;top:44px;font-size:7.5px;line-height:9.5px}
  .letterhead .contact{position:absolute;left:326px;top:66px;color:var(--blue-dark)}
  .letterhead .contact span{color:var(--ink)}
  .letter{position:absolute;left:49px;top:193px;width:394px;font-family:"PT Sans",Arial,sans-serif;color:var(--body-ink)}
  .letter .salutation{font-size:13px;margin-bottom:22px;color:#555}
  .letter p{font-size:7.3px;line-height:11.7px;margin-bottom:11.7px}
  .letter .closing{margin-top:20px}
  .signature{display:block;margin-top:6px}

  /* business card front */
  .card-front{left:578px;top:74px;width:266px;height:152px;background:var(--card-grey)}
  .card-front .panel{position:absolute;inset:0}
  .card-front .person{position:absolute;left:10px;top:38px;color:#fff}
  .card-front .person h2{font-size:9.5px;font-weight:700}
  .card-front .person .role{font-size:7px;margin-top:1px}
  .card-front .addr{font-size:6px;line-height:8px;margin-top:9px}
  .card-front .contact{font-size:6px;line-height:8.4px;margin-top:5px}
  .card-front .wordmark{position:absolute;left:143px;top:71px;font-size:15px}

  /* business card back */
  .card-back{left:877px;top:144px;width:267px;height:152px;background:var(--charcoal);color:#fff;text-align:center}
  .card-back .wordmark{color:#fff;justify-content:center;margin-top:42px;font-size:22px}
  .card-back .wordmark .dot{background:#fff}
  .card-back .slogan{font-size:7.5px;font-weight:700;position:absolute;left:0;right:0;top:126px}

  /* envelope back */
  .envelope-back{left:615px;top:350px;width:547px;height:248px;background:#f0f0f0}
  .envelope-back .flap{position:absolute;left:0;top:0}
  .envelope-back .flap-content{position:absolute;left:0;right:0;top:22px;text-align:center;color:#fff}
  .envelope-back .wordmark{color:#fff;justify-content:center;font-size:15px}
  .envelope-back .wordmark .dot{background:#fff}
  .envelope-back .url{font-size:7.5px;margin-top:6px}

  /* envelope front */
  .envelope-front{left:547px;top:470px;width:549px;height:250px}
  .envelope-front .wordmark{position:absolute;left:22px;top:36px;font-size:19px}
  .envelope-front .return-address{position:absolute;left:38px;top:68px;font-size:7.5px;line-height:9.5px}
</style>
</head>
<body>
<main class="canvas">

  <!-- Letterhead -->
  <section class="sheet letterhead" aria-label="Letterhead">
    <div class="wordmark"><span class="dot"></span><span class="name">CORBROOK<span class="sub">ESTATES LLC</span></span></div>
    <div class="divider"></div>
    <div class="address">2750 Alder Ridge Road #B210<br>Fairview, CA 90417</div>
    <ul class="contact">
      <li><svg viewBox="0 0 10 10"><path fill="currentColor" d="M2 0l2 2-1 2c1 1 2 2 3 3l2-1 2 2-2 2C4 10 0 6 0 2z"/></svg><span>555-014-2286</span></li>
      <li><svg viewBox="0 0 10 10"><rect fill="currentColor" x="2" y="0" width="6" height="3"/><rect fill="currentColor" x="0" y="4" width="10" height="4" rx="1"/></svg><span>555-014-7730</span></li>
      <li><svg viewBox="0 0 10 10"><rect fill="currentColor" x="0" y="2" width="10" height="7"/><path d="M0 2l5 4 5-4" stroke="#fff" fill="none"/></svg><span>dan@corbrookestates.us</span></li>
      <li><svg viewBox="0 0 10 10"><circle fill="currentColor" cx="5" cy="5" r="5"/></svg><span>www.corbrookestates.us</span></li>
    </ul>

    <article class="letter">
      <p class="salutation">Dear Mr. Ellison,</p>
      <p>Lorem ipsum dolor sit amet, consectetur adipiscing elit. Donec orci purus, luctus vitae dignissim eu, iaculis sed purus. Vivamus faucibus, ipsum nec aliquet viverra, leo mauris condimentum ligula, sit amet sagittis enim ligula quis arcu. Nam egestas tortor id nisi porttitor mattis. In tortor ante, ultricies in suscipit a, tempus non massa. Vivamus et auctor mi. Fusce vel massa nulla. Phasellus nec eros mauris, et scelerisque orci.</p>
      <p>Donec malesuada orci vitae nulla accumsan porta a id massa. Quisque accumsan iaculis magna sit amet fringilla. Maecenas consequat, magna eget tincidunt semper, odio nibh rutrum mi, id feugiat ante nisi eu risus. Vestibulum nunc orci, rhoncus a placerat in, ultricies in mi. Cras mattis varius eros, vel fringilla nisi suscipit eget. Quisque scelerisque sagittis nulla at porttitor.</p>
      <p>Sed id augue vitae urna euismod commodo aliquet a quam. Pellentesque arcu velit, cursus et malesuada ut, consequat et diam. Nullam erat sem, rhoncus id ullamcorper vitae, rhoncus et arcu. In ultricies ultricies nulla, ut rutrum nisi iaculis at. Donec eu magna a metus ornare faucibus. Fusce aliquet faucibus ultricies. Morbi semper, est id tincidunt gravida, sem arcu adipiscing lacus, ac bibendum nulla leo eu purus. Quisque nec diam sed risus consectetur a accumsan quis quis nibh. Vestibulum id purus lorem.</p>
      <p>It is a long established fact that a reader will be distracted by the readable content of a page when looking at its layout. The point of using Lorem Ipsum is that it has a more-or-less normal distribution of letters, as opposed to using 'Content here, content here', making it look like readable English. Many desktop publishing packages</p>
      <p class="closing">Sincerely,</p>
      <svg class="signature" width="66" height="26" viewBox="0 0 66 26" aria-hidden="true"><path d="M1 14c15-1 30-2 50-1M12 4c6 0 10 2 12 6s-2 14 0 14 4-6 2-10c-2-3-8-4-12-3M40 18h18" fill="none" stroke="#222" stroke-width="1"/></svg>
    </article>

    <svg class="band" width="488" height="30" viewBox="0 0 488 30" preserveAspectRatio="none" aria-hidden="true">
      <path d="M0 2Q244 16 488 2" fill="none" stroke="#5a5a5a" stroke-width="1.2"/>
      <path d="M0 4Q244 18 488 4V30H0z" fill="var(--blue)"/>
    </svg>
  </section>

  <!-- Business card front -->
  <section class="sheet card-front" aria-label="Business card front">
    <svg class="panel" width="266" height="152" viewBox="0 0 266 152" aria-hidden="true">
      <path d="M0 0H218C150 0 118 60 122 100C125 125 140 145 160 152H0z" fill="var(--blue)"/>
      <path d="M218 0C150 0 118 60 122 100C125 125 140 145 160 152H168C146 140 130 120 130 96C130 50 168 4 246 4C236 1 228 0 218 0z" fill="#3b3b3d"/>
    </svg>
    <div class="person">
      <h2>DANIEL HARLOW</h2>
      <div class="role">Property Manager</div>
      <div class="addr">2750 Alder Ridge Road #B210<br>Fairview, CA 90417</div>
      <ul class="contact">
        <li><svg viewBox="0 0 10 10"><path fill="#fff" d="M2 0l2 2-1 2c1 1 2 2 3 3l2-1 2 2-2 2C4 10 0 6 0 2z"/></svg>555-014-2286</li>
        <li><svg viewBox="0 0 10 10"><rect fill="#fff" x="2" y="0" width="6" height="3"/><rect fill="#fff" x="0" y="4" width="10" height="4" rx="1"/></svg>555-014-7730</li>
        <li><svg viewBox="0 0 10 10"><rect fill="#fff" x="0" y="2" width="10" height="7"/></svg>dan@corbrookestates.us</li>
        <li><svg viewBox="0 0 10 10"><circle fill="#fff" cx="5" cy="5" r="5"/></svg>www.corbrookestates.us</li>
      </ul>
    </div>
    <div class="wordmark"><span class="dot"></span><span class="name">CORBROOK<span class="sub">ESTATES LLC</span></span></div>
  </section>

  <!-- Business card back -->
  <section class="sheet card-back" aria-label="Business card back">
    <div class="wordmark"><span class="dot"></span><span class="name">CORBROOK<span class="sub">ESTATES LLC</span></span></div>
    <p class="slogan">Multifamily Property Management</p>
  </section>

  <!-- Envelope back -->
  <section class="sheet envelope-back" aria-label="Envelope back">
    <svg class="flap" width="547" height="96" viewBox="0 0 547 96" aria-hidden="true">
      <path d="M0 0H547L537 60C534 78 524 90 505 92H42C23 90 13 78 10 60z" fill="#dfe6ea"/>
      <path d="M0 0H547L537 56C534 74 524 86 505 88H42C23 86 13 74 10 56z" fill="var(--charcoal)"/>
    </svg>
    <div class="flap-content">
      <div class="wordmark"><span class="dot"></span><span class="name">CORBROOK<span class="sub">ESTATES LLC</span></span></div>
      <div class="url">www.corbrookestates.us</div>
    </div>
  </section>

  <!-- Envelope front -->
  <section class="sheet envelope-front" aria-label="Envelope front">
    <div class="wordmark"><span class="dot"></span><span class="name">CORBROOK<span class="sub">ESTATES LLC</span></span></div>
    <div class="return-address">2750 Alder Ridge Road #B210<br>Fairview, CA 90417</div>
    <svg class="band" width="549" height="30" viewBox="0 0 549 30" preserveAspectRatio="none" aria-hidden="true">
      <path d="M0 2Q274 16 549 2" fill="none" stroke="#5a5a5a" stroke-width="1.2"/>
      <path d="M0 4Q274 18 549 4V30H0z" fill="var(--blue)"/>
    </svg>
  </section>

</main>
</body>
</html>
```